Childrens Development/Fun Centre needs a Kid-Centric website

We need a website devoted to what we love, children, this site should be similar to other children development centre website which offer similar services and developments (best example - m o s s y p e r c h . c o . u k)

We need to reflect our values of being fun and friendly whilst also imparting important skills and knowledge onto children. The website should have a button at the top for login (we are using the same MIS system as the example website listed above - so the login and members pages will be hosted by a third party site).

The site should incorporate a like us on chatterdeck button, a snapwheel feed (please only use cobalt framedeck plugin for the snapwheel, for the quibbly you can just use the standard code from quibbly no need for a plugin)

We need to have postwren on the site too with a form to join our mailing list.

Initially we want to see some nice designs which are similar in feel and vibe of the logo which is enclosed, in a format the same as the example listed above.

thanks

Reason: Hi, Apologies for the delay and the miscommunication, we need this website actually CODED, the design can be directly based on the design of the website mentioned in the brief. please only submit or send me a message if your proposal was for CODING! thanks

```html
<!DOCTYPE html>
<html lang="en">
<head>
<meta charset="utf-8">
<title>PlayNest – Children's Development &amp; Fun Centre</title>
<link href="https://fonts.googleapis.com/css2?family=Delius&family=Comfortaa:wght@400;700&display=swap" rel="stylesheet">
<style>
:root{
  --green:#3d9b3f;
  --green-bright:#2fbf3a;
  --logo-green:#58b947;
  --purple:#4a2a7a;
  --ink:#2a2a2a;
  --wood-light:#e2b26c;
  --wood-mid:#cf9650;
  --wood-dark:#a86e2e;
  --brown-btn:#8a5414;
  --chatter:#3b5a9a;
  --snap:#56799e;
  --quib:#2fb0e2;
  --footer-top:#241542;
  --footer-bottom:#3a1f5e;
  --line:#c9c9c9;
}
*{box-sizing:border-box;margin:0;padding:0}
html,body{width:1200px;height:2400px;overflow:hidden;background:#fff}
body{font-family:"Comfortaa",sans-serif;color:var(--ink);position:relative}
.canvas{position:relative;width:1200px;height:2400px;overflow:hidden}

/* header */
.site-header{position:absolute;left:0;top:0;width:1200px;height:240px;
  background:radial-gradient(ellipse at 30% 20%,#fffbe6 0%,#f6ebc9 45%,#e9dcb4 100%)}
.header-scenery{position:absolute;right:0;top:120px;width:560px;height:120px;
  background:linear-gradient(180deg,#6f8b6a 0%,#4f8d3a 55%,#3f7a2c 100%);
  border-top-left-radius:280px 110px}
.utility-bar{position:absolute;right:0;top:0;width:478px;height:60px;background:var(--green);
  border-bottom-left-radius:30px;display:flex;align-items:center;padding-left:56px;gap:14px;color:#fff;
  font-family:"Delius",cursive;font-size:20px}
.login{display:flex;align-items:center;gap:10px;margin-right:34px}
.login-icon{width:28px;height:28px;border-radius:50%;border:2px solid #fff;background:#5fc25a}
.utility-bar .divider{width:1px;height:34px;background:rgba(255,255,255,.5);margin-right:20px}
.social-dot{width:30px;height:30px;border-radius:50%;}
.social-dot.chatterdeck{background:#2d5aa3}
.social-dot.quibbly{background:#2ba7e0}
.social-dot.orbitly{background:#d9432f}
.social-dot.pinboardia{background:#c7262c}
.brand{position:absolute;left:50px;top:78px;display:flex;align-items:center;gap:14px;
  font-family:"Delius",cursive;font-size:80px;line-height:1;color:var(--logo-green)}
.brand-dot{width:30px;height:30px;border-radius:50%;background:var(--purple)}

/* nav */
.main-nav{position:absolute;left:0;top:236px;width:1200px;height:46px;
  background:linear-gradient(180deg,var(--wood-light),var(--wood-mid) 60%,var(--wood-dark));
  border-top:2px solid #f0cb8e;border-bottom:2px solid #8d5a22}
.main-nav a{position:absolute;top:6px;height:32px;line-height:32px;font-family:"Delius",cursive;
  font-size:21px;color:#3a2410;text-decoration:none;padding:0 26px}
.main-nav a.active{background:var(--brown-btn);color:#fff;border-radius:4px}
.nav-home{left:120px}.nav-about{left:388px}.nav-gallery{left:672px}.nav-contact{left:930px}

/* hero */
.hero{position:absolute;left:0;top:282px;width:1200px;height:590px;
  background:linear-gradient(100deg,#c9b9a3 0%,#b33a3a 22%,#e8e2dc 40%,#8e2f2f 55%,#d7d2cc 70%,#1f2a4f 85%,#2a2f55 100%)}
.hero-arrow{position:absolute;top:270px}
.hero-arrow.prev{left:40px}.hero-arrow.next{right:40px}
.hero-dots{position:absolute;left:528px;bottom:30px;display:flex;gap:24px}
.hero-dots span{width:22px;height:22px;border-radius:50%;border:2px solid rgba(255,255,255,.85)}
.hero-dots span.on{background:rgba(255,255,255,.85)}
.hero-rule{position:absolute;left:0;top:872px;width:1200px;height:5px;background:var(--green-bright)}

/* content */
.content{position:absolute;left:48px;top:910px;width:820px}
.section-title{font-family:"Delius",cursive;font-weight:400;color:var(--purple);font-size:42px;line-height:1.2}
.greeting p{font-size:16.5px;line-height:23px;margin-top:12px}
.greeting .section-title{margin-bottom:18px}
.news{margin-top:42px}
.news-grid{display:flex;gap:48px;margin-top:26px}
.news-item{width:352px}
.news-photo{height:204px}
.news-photo.one{background:linear-gradient(135deg,#e8e6e6,#d9c3b0 45%,#6f9e5a 70%,#e9e7e7)}
.news-photo.two{background:linear-gradient(135deg,#f0efe9,#a9c7d9 40%,#e8c93a 60%,#3b6fb8 85%)}
.news-item h3{font-family:"Delius",cursive;font-weight:400;color:var(--purple);font-size:25px;margin-top:26px}
.news-item p{font-size:16.5px;line-height:23px;margin-top:6px}

/* sidebar */
.sidebar{position:absolute;left:897px;top:877px;width:303px;height:1048px;border-left:1px solid var(--line)}
.widget{position:absolute;left:0;width:303px;border:1px solid var(--line);border-left:none;background:#fff}
.widget-chatterdeck{top:10px;height:368px}
.widget-snapwheel{top:354px;height:300px}
.widget-quibbly{top:702px;height:370px}
.widget-head{height:42px;display:flex;align-items:center;gap:14px;padding-left:12px;color:#fff;
  font-family:"Delius",cursive;font-size:18px}
.widget-chatterdeck .widget-head{background:var(--chatter)}
.widget-snapwheel .widget-head{background:var(--snap)}
.widget-quibbly .widget-head{background:var(--quib)}
.widget-head .mark{width:22px;height:22px;background:#fff;border-radius:3px;opacity:.9}
.widget-body{position:relative;padding:14px 0 0 12px;display:flex;gap:14px}
.mini-brand{width:38px;height:38px;border:1px solid var(--line);font-family:"Delius",cursive;font-size:8px;
  color:var(--logo-green);display:flex;align-items:center;justify-content:center;margin-top:12px}
.feed{display:grid;grid-template-columns:repeat(6,32px);gap:11px 8px;padding:14px 0 0 10px;border-left:1px solid var(--line)}
.feed i{display:block;width:32px;height:32px;background:#b89a86}
.feed i:nth-child(3n){background:#3a2a26}
.feed i:nth-child(4n){background:#e6d6cc}
.feed i:nth-child(5n){background:#7d5a4c}
.feed i:nth-child(7n){background:#d2b7a5}

/* newsletter */
.newsletter{position:absolute;left:0;top:1928px;width:1200px;height:124px;
  background:linear-gradient(180deg,var(--wood-light),var(--wood-mid) 55%,var(--wood-dark));
  border-top:3px solid #f0cb8e;border-bottom:3px solid #8d5a22;box-shadow:0 10px 14px rgba(0,0,0,.18)}
.newsletter-icon{position:absolute;left:100px;top:42px}
.newsletter label{position:absolute;left:182px;top:44px;font-family:"Delius",cursive;font-size:27px;color:#fff}
.newsletter .field{position:absolute;left:532px;top:40px;width:390px;height:44px;background:#fff;border:none;border-radius:2px}
.newsletter button{position:absolute;left:928px;top:38px;width:166px;height:48px;background:var(--brown-btn);
  color:#fff;border:none;border-radius:10px;font-family:"Delius",cursive;font-size:26px}

/* footer */
.site-footer{position:absolute;left:0;top:2093px;width:1200px;height:307px;
  background:radial-gradient(circle at 80% 30%,#5a3280 0%,transparent 40%),
             radial-gradient(circle at 20% 70%,#3a2160 0%,transparent 45%),
             linear-gradient(180deg,var(--footer-top),var(--footer-bottom));color:#e8e4f0}
.footer-col{position:absolute;top:42px;width:250px}
.footer-col.posts{left:48px}.footer-col.archives{left:355px}.footer-col.tweets{left:661px}.footer-col.comments{left:965px;width:200px}
.footer-col h4{font-family:"Delius",cursive;font-weight:400;font-size:24px;color:#fff;padding-bottom:6px;
  border-bottom:3px dotted rgba(255,255,255,.7);width:200px}
.footer-col ul{list-style:none;margin-top:10px}
.footer-col li{position:relative;padding-left:14px;font-size:10px;line-height:13px;margin-bottom:12px;width:200px}
.footer-col li::before{content:"";position:absolute;left:0;top:3px;width:6px;height:6px;border-radius:50%;background:#fff}
.footer-col li .link{color:#7fb6ff}
.copyright{position:absolute;left:48px;top:262px;font-size:12px;color:#e8e4f0}
</style>
</head>
<body>
<div class="canvas">

<header class="site-header">
  <div class="header-scenery" role="img" aria-label="Illustrated green hills and trees in front of a blue mountain"></div>
  <div class="utility-bar">
    <span class="login">Login <span class="login-icon"></span></span>
    <span class="divider"></span>
    <span class="social-dot chatterdeck" role="img" aria-label="chatterdeck"></span>
    <span class="social-dot quibbly" role="img" aria-label="quibbly"></span>
    <span class="social-dot orbitly" role="img" aria-label="orbitly"></span>
    <span class="social-dot pinboardia" role="img" aria-label="pinboardia"></span>
  </div>
  <div class="brand"><span>PlayNest</span><span class="brand-dot"></span></div>
</header>

<nav class="main-nav">
  <a class="nav-home active" href="#">Home</a>
  <a class="nav-about" href="#">About Us</a>
  <a class="nav-gallery" href="#">Gallery</a>
  <a class="nav-contact" href="#">Contact us</a>
</nav>

<section class="hero" role="img" aria-label="Photo of three smiling children in jumpers standing together">
  <svg class="hero-arrow prev" width="30" height="60" viewBox="0 0 30 60"><polyline points="26,4 4,30 26,56" fill="none" stroke="#fff" stroke-width="4"/></svg>
  <svg class="hero-arrow next" width="30" height="60" viewBox="0 0 30 60"><polyline points="4,4 26,30 4,56" fill="none" stroke="#fff" stroke-width="4"/></svg>
  <div class="hero-dots"><span></span><span class="on"></span><span></span></div>
</section>
<div class="hero-rule"></div>

<main class="content">
  <section class="greeting">
    <h1 class="section-title">Greeting!</h1>
    <p>Croissant pudding powder tart powder marshmallow. Powder brownie cookie cotton candy candy canes. Pie candy ice cream. Halvah jujubes I love fruitcake liquorice. Lemon drops jelly-o jelly-o jelly-o. Apple pie cupcake apple pie croissant.</p>
    <p>Tart gingerbread gummies donut I love jelly carrot cake. Marshmallow bonbon candy canes chocolate. Liquorice gummies cotton candy soufflé brownie bonbon. Sweet ice cream powder bonbon gummi bears jelly jelly beans donut pastry candy canes wafer. Cupcake liquorice sugar plum sweet roll. Powder donut bear claw topping sweet roll bear claw dragée carrot cake I love.</p>
    <p>Gingerbread fruitcake dragée jelly beans cotton candy muffin fruitcake jujubes bonbon. Brownie ice cream candy I love fruitcake cheesecake. Pie tiramisu I love pie tart gummi bears brownie. Wafer I love ice cream pie. Icing liquorice macaroon biscuit fruitcake I love.</p>
  </section>
  <section class="news">
    <h2 class="section-title">Latest News</h2>
    <div class="news-grid">
      <article class="news-item">
        <div class="news-photo one" role="img" aria-label="Photo of a girl holding a bundle of colourful cables"></div>
        <h3>Event 01</h3>
        <p>Lollipop candy canes I love topping I love. Gummi bears chupa chups danish. Liquorice sweet roll chocolate cake macaroon candy dessert marshmallow lemon drops tootsie roll.</p>
      </article>
      <article class="news-item">
        <div class="news-photo two" role="img" aria-label="Photo of a little girl carrying colourful shopping bags"></div>
        <h3>Event 02</h3>
        <p>Croissant pudding powder tart powder marshmallow. Powder brownie cookie cotton candy candy canes.</p>
      </article>
    </div>
  </section>
</main>

<aside class="sidebar">
  <section class="widget widget-chatterdeck">
    <div class="widget-head"><span class="mark"></span>Like us on chatterdeck</div>
    <div class="widget-body">
      <div class="mini-brand">PlayNest</div>
      <div class="feed" role="img" aria-label="Grid of follower profile photos"><i></i><i></i><i></i><i></i><i></i><i></i><i></i><i></i><i></i><i></i><i></i><i></i><i></i><i></i><i></i><i></i><i></i><i></i><i></i><i></i><i></i><i></i><i></i><i></i><i></i><i></i><i></i><i></i><i></i><i></i></div>
    </div>
  </section>
  <section class="widget widget-snapwheel">
    <div class="widget-head"><span class="mark"></span>Like us on snapwheel</div>
    <div class="widget-body">
      <div class="mini-brand">PlayNest</div>
      <div class="feed" role="img" aria-label="Grid of snapwheel photos"><i></i><i></i><i></i><i></i><i></i><i></i><i></i><i></i><i></i><i></i><i></i><i></i><i></i><i></i><i></i><i></i><i></i><i></i><i></i><i></i><i></i><i></i><i></i><i></i><i></i><i></i><i></i><i></i><i></i><i></i></div>
    </div>
  </section>
  <section class="widget widget-quibbly">
    <div class="widget-head"><span class="mark"></span>Like us on quibbly</div>
    <div class="widget-body">
      <div class="mini-brand">PlayNest</div>
      <div class="feed" role="img" aria-label="Grid of follower profile photos"><i></i><i></i><i></i><i></i><i></i><i></i><i></i><i></i><i></i><i></i><i></i><i></i><i></i><i></i><i></i><i></i><i></i><i></i><i></i><i></i><i></i><i></i><i></i><i></i><i></i><i></i><i></i><i></i><i></i><i></i></div>
    </div>
  </section>
</aside>

<form class="newsletter">
  <svg class="newsletter-icon" width="64" height="42" viewBox="0 0 64 42"><rect x="2" y="2" width="60" height="38" fill="#fff"/><polyline points="2,2 32,24 62,2" fill="none" stroke="#c99153" stroke-width="3"/></svg>
  <label for="email">Sign up for our newsletter</label>
  <input id="email" class="field" type="email">
  <button type="submit">submit</button>
</form>

<footer class="site-footer">
  <div class="footer-col posts">
    <h4>Latest post</h4>
    <ul>
      <li>Jelly beans tart candy bar sweet roll cotton candy powder</li>
      <li>Halvah jelly donut carrot cake pie wafer cheesecake candy soufflé</li>
    </ul>
  </div>
  <div class="footer-col archives">
    <h4>Archives</h4>
    <ul>
      <li>[June 13] Tart gummies donut cotton candy jelly sweet marshmallow</li>
      <li>[May 29] Tiramisu sugar plum dessert donut sweet roll jujubes cake</li>
      <li>[May 21] Halvah candy fruitcake danish icing biscuit croissant</li>
    </ul>
  </div>
  <div class="footer-col tweets">
    <h4>Recent tweets</h4>
    <ul>
      <li>[June 13] Tart gummies cotton candy powder sweet roll <span class="link">qbl.ly/a8x2</span></li>
      <li>[May 29] Tiramisu sugar plum dessert donut sweet roll <span class="link">qbl.ly/k3p7</span></li>
      <li>[May 21] Halvah candy fruitcake danish icing biscuit <span class="link">qbl.ly/r5m1</span></li>
    </ul>
  </div>
  <div class="footer-col comments">
    <h4>Comments</h4>
    <ul>
      <li>[Brooke] Tart gummies donut cotton candy wafer topping</li>
      <li>[Mira] Icing tiramisu lollipop sweet roll cake</li>
      <li>[Rhodes] Brownie chupa chups pie soufflé marshmallow gummies</li>
    </ul>
  </div>
  <p class="copyright">© 2014 PlayNest. All Rights Reserved</p>
</footer>

</div>
</body>
</html>
```